Vehicle graphics for healthcare company (bluecrestcare.co.uk)

I have a plain white van that needs some branding. I don't mind leaving a bit of the white, so I would consider a half wrap, or large panels of non-white, but I'm open to suggestion.

For a non-wrap design, I happened to see the KDO Van (attached photo), which I thought was a nice clear design. I thought maybe some elements of this could be included. Maybe their large A could be the S of my Blue Crest logo.

The only two colours the company has used to date are the green and grey of the logo. 1B7F8C and 58585A.

The core business we provide is assessment for people about to purchase a wheelchair. We take their measurements, look at their clinical needs and then recommend a product for them to purchase.

The information we need on it:
- our logo (attached)
- Private Wheelchair Assessment
- Occupational Therapy
- Wheelchair Skills

Our contact details to be included:
- www.bluecrestcare.co.uk
- info@bluecrestcare.co.uk
- 02937 418205

Target Market(s)

Wheelchair users and other healthcare providers.

Industry/Entity Type

Healthcare

Font styles to use
Other font styles liked:
• Arthaus Medium

Requirements
Must have
• Logo, contact details. Green/grey colours. 1B7F8C and 58585A
Nice to have
• See attached van, I thought this was a simple, clear design.
Should not have
• Clutter.

```html
<!DOCTYPE html>
<html lang="en">
<head>
<meta charset="utf-8">
<title>Blue Crest Therapy – Van Livery</title>
<link href="https://fonts.googleapis.com/css2?family=Comfortaa:wght@700&family=Poppins:ital,wght@1,700&display=swap" rel="stylesheet">
<style>
  :root{
    --teal:#1B7F8C;
    --grey:#58585A;
    --body:#ffffff;
    --outline:#c9cbcd;
    --glass:#8d9196;
    --tread:#e4e5e6;
    --page:#ffffff;
  }
  html,body{margin:0;padding:0;width:1200px;height:1200px;overflow:hidden;background:var(--page);}
  .livery{display:block;width:1200px;height:1200px;}
  .van-body{fill:var(--body);stroke:var(--outline);stroke-width:2;}
  .van-glass{fill:var(--glass);}
  .arch{fill:none;stroke:var(--outline);stroke-width:2;}
  .tread-graphic{fill:var(--tread);}
  .stripe-grey{fill:none;stroke:var(--grey);stroke-width:6;}
  .stripe-teal{fill:none;stroke:var(--teal);stroke-width:2;}
  .wedge{fill:var(--teal);}
  .brand-name{font-family:'Comfortaa',sans-serif;font-weight:700;font-size:54px;fill:var(--teal);letter-spacing:1px;}
  .brand-sub{font-family:'Comfortaa',sans-serif;font-weight:700;font-size:34px;fill:var(--grey);letter-spacing:2px;}
  .phone{font-family:'Comfortaa',sans-serif;font-weight:700;font-size:40px;fill:#fff;stroke:var(--teal);stroke-width:2.5;}
  .web{font-family:'Poppins',sans-serif;font-style:italic;font-weight:700;font-size:20px;fill:var(--teal);}
  .service-bar{fill:var(--teal);}
  .service-text{font-family:'Comfortaa',sans-serif;font-weight:700;font-size:11px;fill:#fff;letter-spacing:.3px;}
  .social-dot{fill:var(--teal);}
  .email{font-family:'Comfortaa',sans-serif;font-weight:700;font-size:5px;fill:var(--grey);}
</style>
</head>
<body>
<svg class="livery" viewBox="0 0 1200 1200" xmlns="http://www.w3.org/2000/svg">
  <defs>
    <path id="van-shape" d="M138,470 L140,405 Q148,372 230,332 L330,300 L428,202 Q448,188 480,186 L1020,186 Q1046,188 1050,215 L1058,460 L1058,505 L955,505 A76,76 0 0 0 800,505 L385,505 A76,76 0 0 0 235,505 L145,505 Z"/>
    <clipPath id="clip-left-facing"><use href="#van-shape"/></clipPath>
    <clipPath id="clip-right-facing"><use href="#van-shape" transform="translate(1186,505) scale(-1,1)"/></clipPath>
  </defs>

  <g class="van-side van-side--nearside">
    <use href="#van-shape" class="van-body"/>
    <g clip-path="url(#clip-left-facing)">
      <rect class="tread-graphic" x="840" y="186" width="220" height="320" role="img" aria-label="Faint grey wheelchair tyre-track graphic"/>
      <polygon class="van-glass" points="345,305 425,210 530,205 530,312"/>
      <polyline class="stripe-grey" points="395,505 800,345 1060,330"/>
      <polyline class="stripe-teal" points="505,505 800,392 1060,385"/>
      <polygon class="wedge" points="650,505 800,455 800,505"/>
    </g>
    <path class="arch" d="M235,505 A76,76 0 0 1 385,505 M800,505 A76,76 0 0 1 955,505"/>

    <g class="services">
      <rect class="service-bar" x="778" y="222" width="262" height="17"/>
      <text class="service-text" x="786" y="234">• PRIVATE WHEELCHAIR ASSESSMENT</text>
      <rect class="service-bar" x="808" y="242" width="232" height="17"/>
      <text class="service-text" x="816" y="254">• OCCUPATIONAL THERAPY</text>
      <rect class="service-bar" x="838" y="262" width="202" height="17"/>
      <text class="service-text" x="846" y="274">• WHEELCHAIR SKILLS</text>
    </g>

    <g class="socials">
      <circle class="social-dot" cx="262" cy="362" r="5.5"/>
      <circle class="social-dot" cx="277" cy="362" r="5.5"/>
      <circle class="social-dot" cx="292" cy="362" r="5.5"/>
      <circle class="social-dot" cx="307" cy="362" r="5.5"/>
      <text class="email" x="256" y="377">info@bluecrestcare.co.uk</text>
    </g>

    <text class="brand-name" x="400" y="420" transform="rotate(-20 400 420)">BLUE CREST</text>
    <text class="brand-sub" x="500" y="445" transform="rotate(-20 500 445)">THERAPY</text>
    <text class="phone" x="520" y="490" transform="rotate(-20 520 490)">02937 418205</text>
    <text class="web" x="594" y="494" transform="rotate(-20 594 494)">bluecrestcare.co.uk</text>
  </g>

  <g class="van-side van-side--offside">
    <use href="#van-shape" class="van-body" transform="translate(1186,505) scale(-1,1)"/>
    <g clip-path="url(#clip-right-facing)">
      <rect class="tread-graphic" x="126" y="691" width="220" height="320" role="img" aria-label="Faint grey wheelchair tyre-track graphic"/>
      <polygon class="van-glass" points="841,810 761,715 656,710 656,817"/>
      <polyline class="stripe-grey" points="791,1010 386,850 126,835"/>
      <polyline class="stripe-teal" points="681,1010 386,897 126,890"/>
      <polygon class="wedge" points="536,1010 386,960 386,1010"/>
    </g>
    <path class="arch" d="M801,1010 A76,76 0 0 1 951,1010 M231,1010 A76,76 0 0 1 386,1010"/>

    <g class="services">
      <rect class="service-bar" x="146" y="727" width="262" height="17"/>
      <text class="service-text" x="156" y="739">• PRIVATE WHEELCHAIR ASSESSMENT</text>
      <rect class="service-bar" x="146" y="747" width="232" height="17"/>
      <text class="service-text" x="196" y="759">• OCCUPATIONAL THERAPY</text>
      <rect class="service-bar" x="146" y="767" width="202" height="17"/>
      <text class="service-text" x="196" y="779">• WHEELCHAIR SKILLS</text>
    </g>

    <g class="socials">
      <circle class="social-dot" cx="879" cy="867" r="5.5"/>
      <circle class="social-dot" cx="894" cy="867" r="5.5"/>
      <circle class="social-dot" cx="909" cy="867" r="5.5"/>
      <circle class="social-dot" cx="924" cy="867" r="5.5"/>
      <text class="email" x="872" y="882">info@bluecrestcare.co.uk</text>
    </g>

    <text class="brand-name" x="462" y="807" transform="rotate(20 462 807)">BLUE CREST</text>
    <text class="brand-sub" x="506" y="885" transform="rotate(20 506 885)">THERAPY</text>
    <text class="phone" x="375" y="889" transform="rotate(20 375 889)">02937 418205</text>
    <text class="web" x="359" y="913" transform="rotate(20 359 913)">bluecrestcare.co.uk</text>
  </g>
</svg>
</body>
</html>
```